Mosque App design fresh look and feel

Need to create a mosque app which has half a couple of dozen pages, a login page will take you into the main information with about 6 categories, such as school, memberships, information, prayer times etc... we have 3 types of users... 1. User .. admin user 3. imam user

I have xd files available.
https://mocks.plarvio.com/view/e4f7a2d1-8b3c-4f6e-a9d2-71b5c3e8f046-2ac7/

Target Market(s)

Muslims

Font styles to use
Sans Serif

Requirements
Must have
• Great UI
Simple flow

```html
<!DOCTYPE html>
<html lang="en">
<head>
<meta charset="utf-8">
<title>Welcome – Prayer time</title>
<link rel="stylesheet" href="https://fonts.googleapis.com/css2?family=Open+Sans:wght@400;600;700&display=swap">
<style>
  :root {
    --brand-green: #22c47a;
    --ink: #111111;
    --ink-soft: #333333;
    --placeholder: #c4c4c4;
    --divider: #e6e6e6;
    --rule: #9a9a9a;
    --field-border: #cfcfcf;
    --link: #2a8fd8;
    --paper: #ffffff;
    --scroll-track: #eeeeee;
    --scroll-thumb: #c8c8c8;
  }
  * { box-sizing: border-box; margin: 0; padding: 0; }
  html, body {
    width: 1200px; height: 2598px; overflow: hidden;
    background: var(--paper);
    font-family: "Open Sans", sans-serif; color: var(--ink);
  }
  .screen {
    position: absolute; left: 0; top: 0;
    width: 375px; height: 812px;
    transform: scale(3.2); transform-origin: 0 0;
  }
  .abs { position: absolute; }

  .brand-mark {
    left: 30px; top: 50px; width: 55px; height: 55px;
    background: var(--brand-green); border-radius: 4px;
    color: var(--paper); font-size: 11px; font-weight: 700;
    display: flex; align-items: center; justify-content: center;
  }
  .welcome-title {
    left: 105px; top: 60px; font-size: 23px; font-weight: 700;
    letter-spacing: 1.2px; line-height: 36px;
  }
  .section-label { font-size: 12px; letter-spacing: .4px; color: var(--ink-soft); }

  .field {
    left: 30px; width: 315px; height: 44px;
    background: var(--paper); border-radius: 4px;
    box-shadow: 0 1px 6px rgba(0,0,0,.14);
    padding-left: 10px; display: flex; align-items: center;
    font-size: 11px; color: var(--placeholder); letter-spacing: .3px;
  }
  .field--outlined { box-shadow: none; border: 1.5px solid var(--field-border); }

  .account-note { left: 30px; top: 320px; font-size: 9.5px; color: var(--ink); }
  .account-note a { color: var(--link); text-decoration: underline; }

  .signup-button {
    left: 243px; top: 301px; width: 102px; height: 45px;
    background: var(--brand-green); color: var(--paper);
    border-radius: 4px; box-shadow: 0 1px 5px rgba(0,0,0,.15);
    font-size: 13.5px; font-weight: 700; letter-spacing: .8px;
    display: flex; align-items: center; justify-content: center;
  }

  .provider-list { left: 30px; top: 393px; display: flex; gap: 14px; }
  .provider {
    display: flex; align-items: center; gap: 4px;
    font-size: 11px; font-weight: 600; color: var(--ink-soft);
  }
  .provider-dot { width: 20px; height: 20px; border-radius: 50%; background: var(--divider); }

  .rule { left: 30px; top: 423px; width: 315px; height: 1px; background: var(--rule); }

  .prayer-title {
    left: 30px; top: 438px; font-size: 23px; font-weight: 700;
    letter-spacing: 1.2px; line-height: 36px;
  }

  .prayer-card {
    left: 30px; top: 545px; width: 315px; height: 238px;
    background: var(--paper); border-radius: 4px;
    box-shadow: 0 1px 6px rgba(0,0,0,.14); overflow: hidden;
  }
  .prayer-list { list-style: none; position: absolute; left: 15px; top: 0; width: 266px; }
  .prayer-row {
    height: 41px; display: flex; justify-content: space-between; align-items: center;
    font-size: 11.5px; letter-spacing: .4px; color: var(--ink);
    border-bottom: 1px solid var(--divider); padding-top: 5px;
  }
  .prayer-row:first-child { height: 43px; }
  .prayer-row .time { padding-right: 0; }
  .scroll-track {
    left: 300px; top: 13px; width: 4px; height: 215px;
    background: var(--scroll-track); border-radius: 2px;
  }
  .scroll-thumb {
    left: 0; top: 0; width: 4px; height: 114px;
    background: var(--scroll-thumb); border-radius: 2px;
  }
</style>
</head>
<body>
<main class="screen">
  <div class="abs brand-mark">Logo</div>
  <h1 class="abs welcome-title">Welcome</h1>

  <p class="abs section-label" style="left:30px;top:135px;">Sign up</p>
  <div class="abs field" style="top:171px;">Name</div>
  <div class="abs field" style="top:236px;">Email</div>

  <p class="abs account-note">Already have an account? <a href="#">Login</a></p>
  <div class="abs signup-button">Sign up</div>

  <p class="abs section-label" style="left:30px;top:362px;">Sign up with</p>
  <div class="abs provider-list">
    <span class="provider"><span class="provider-dot"></span>Gleam</span>
    <span class="provider"><span class="provider-dot"></span>Facet</span>
  </div>

  <div class="abs rule"></div>

  <h2 class="abs prayer-title">Prayer time</h2>
  <div class="abs field field--outlined" style="top:485px;">Location</div>

  <section class="abs prayer-card">
    <ul class="prayer-list">
      <li class="prayer-row"><span>FAJR</span><span class="time">04:27 AM</span></li>
      <li class="prayer-row"><span>SUNRISE</span><span class="time">05:48 AM</span></li>
      <li class="prayer-row"><span>DHUHR</span><span class="time">12:02 PM</span></li>
      <li class="prayer-row"><span>ASR</span><span class="time">03:24 PM</span></li>
      <li class="prayer-row"><span>MAGHRIB</span><span class="time">06:15 PM</span></li>
    </ul>
    <div class="abs scroll-track"><div class="abs scroll-thumb"></div></div>
  </section>
</main>
</body>
</html>
```